POLITICAL CARD TO HAND OUT

A LITTLE LARGER THAN THE REGULAR BUSINESS CARD WITH THE ABOVE INFORMATION.

Industry/Entity Type

Business

Contact Information for Business Card

ELECT *DEAN HOLT* FOR JUSTICE OF THE PEACE PCT 6-EXPERIENCED LEADERSHIP- WITH MY PICTURE ON IT- PHONE 347-610-2853-MERIDIAN PRIMARY - EARLY VOTING FEB 18TH THRU FEB 28 AND ELECTION DAY IS MARCH 4TH, 2014- USE RED WHITE AND BLUE WITH SOME STARS.

Requirements
Must have
• A FIVE POINTED STAR ON EACH SIDE OF MY NAME

```html
<!DOCTYPE html>
<html lang="en">
<head>
<meta charset="utf-8">
<title>Dean Holt for Justice of the Peace Pct. 6</title>
<link rel="stylesheet" href="https://fonts.googleapis.com/css2?family=Source+Sans+3:wght@400&family=Pinyon+Script&display=swap">
<style>
  :root {
    --ink: #231f20;
    --paper: #ffffff;
    --flag-red: #d6303a;
    --flag-rose: #f3b8a6;
    --flag-blue: #2c3568;
    --flag-haze: #e9e4ec;
    --suit: #1c1c22;
    --skin: #b98577;
    --hat: #e8e6df;
  }
  html, body {
    margin: 0;
    padding: 0;
    overflow: hidden;
    background: var(--paper);
  }
  .card {
    position: relative;
    width: 1200px;
    height: 702px;
    overflow: hidden;
    background: var(--paper);
    font-family: "Source Sans 3", "Myriad Pro", Arial, sans-serif;
    color: var(--ink);
  }
  .flag-backdrop {
    position: absolute;
    inset: 0;
    background:
      linear-gradient(90deg, var(--paper) 0%, var(--paper) 18%, rgba(255,255,255,0.55) 38%, rgba(255,255,255,0) 60%),
      linear-gradient(160deg, var(--flag-haze) 0%, var(--flag-blue) 22%, rgba(44,53,104,0) 38%),
      linear-gradient(170deg, var(--paper) 30%, var(--flag-red) 42%, var(--paper) 52%, var(--flag-red) 64%, var(--flag-rose) 76%, var(--flag-red) 90%);
  }
  .portrait {
    position: absolute;
    left: 700px;
    top: 0;
    width: 500px;
    height: 702px;
    background: linear-gradient(180deg, var(--hat) 0%, var(--hat) 22%, var(--skin) 40%, var(--skin) 55%, var(--suit) 75%, var(--suit) 100%);
  }
  .name-row {
    position: absolute;
    left: 61px;
    top: 40px;
    display: flex;
    align-items: center;
    gap: 30px;
  }
  .star { width: 72px; height: 68px; display: block; }
  .candidate-name {
    margin: 0;
    font-weight: 400;
    font-size: 74px;
    line-height: 1;
    letter-spacing: -0.5px;
  }
  .for {
    position: absolute;
    left: 290px;
    top: 148px;
    font-family: "Pinyon Script", cursive;
    font-size: 26px;
  }
  .office {
    position: absolute;
    left: 66px;
    top: 190px;
    margin: 0;
    font-weight: 400;
    font-size: 54px;
    line-height: 1;
  }
  .slogan {
    position: absolute;
    left: 61px;
    top: 272px;
    margin: 0;
    font-family: "Pinyon Script", cursive;
    font-size: 48px;
    line-height: 72px;
  }
  .ballot-box {
    position: absolute;
    left: 44px;
    top: 445px;
    width: 664px;
    height: 141px;
    box-sizing: border-box;
    border: 1.2px solid var(--ink);
    border-radius: 18px;
    padding: 8px 0 0 21px;
    font-size: 36px;
    line-height: 40px;
  }
  .ballot-box p { margin: 0; }
  .phone {
    position: absolute;
    left: 66px;
    top: 620px;
    margin: 0;
    font-size: 40px;
    line-height: 1;
  }
</style>
</head>
<body>
<svg width="0" height="0" style="position:absolute" aria-hidden="true">
  <defs>
    <radialGradient id="gold-fill" cx="45%" cy="40%" r="65%">
      <stop offset="0" stop-color="#fff2b0"/>
      <stop offset="0.55" stop-color="#f2c230"/>
      <stop offset="1" stop-color="#d49a12"/>
    </radialGradient>
    <symbol id="five-point-star" viewBox="0 0 100 95">
      <polygon points="50,2 62,36 98,36 69,58 80,93 50,72 20,93 31,58 2,36 38,36"
               fill="url(#gold-fill)" stroke="#d49a12" stroke-width="2" stroke-linejoin="round"/>
    </symbol>
  </defs>
</svg>

<main class="card">
  <div class="flag-backdrop" role="img" aria-label="Waving red, white and blue flag backdrop fading to white on the left"></div>
  <div class="portrait" role="img" aria-label="Portrait photo of the candidate in a white cowboy hat and dark suit"></div>

  <div class="name-row">
    <svg class="star" aria-hidden="true"><use href="#five-point-star"/></svg>
    <h1 class="candidate-name">Dean Holt</h1>
    <svg class="star" aria-hidden="true"><use href="#five-point-star"/></svg>
  </div>

  <span class="for">for</span>
  <h2 class="office">Justice of the Peace Pct. 6</h2>

  <p class="slogan">Experienced Leadership for<br>Sable County, Marlow, Texas</p>

  <section class="ballot-box">
    <p>Meridian Primary Ballot:</p>
    <p>Early voting Feb 18th - 28th</p>
    <p>Election March 4th, 2014</p>
  </section>

  <p class="phone">Phone: 347-610-2853</p>
</main>
</body>
</html>
```